bright frame masters

we are a window and door installation company for residential and commercial buildings

These cards are for Colin Mercer
His email is colin@brightframemastersco.com and he is a project manager.

Are colors are white red and black

I want all of his information on the card and a few pictures of windows and doors

```html
<!DOCTYPE html>
<html lang="en">
<head>
<meta charset="utf-8">
<title>Bright Frame Masters – Business Card</title>
<link href="https://fonts.googleapis.com/css2?family=Tinos:wght@400;700&display=swap" rel="stylesheet">
<style>
  :root {
    --brand-red: #a8193a;
    --card-white: #ffffff;
    --ink: #2a2a2a;
    --backdrop: #c8c8c8;
    --photo-warm: #d9c3a5;
    --photo-green: #7f9d5c;
    --photo-pale: #e4e1dc;
    --photo-grey: #9aa0a2;
    --photo-sky: #b9d3d6;
  }
  * { box-sizing: border-box; margin: 0; padding: 0; }
  html, body { width: 1200px; height: 802px; overflow: hidden; }
  body {
    background: var(--backdrop);
    font-family: "Tinos", "Times New Roman", serif;
    position: relative;
  }
  .card {
    position: absolute;
    top: 251px;
    width: 525px;
    height: 300px;
    border-radius: 18px;
    overflow: hidden;
    box-shadow: 0 6px 18px rgba(0,0,0,0.25);
  }
  /* Front */
  .card-front { left: 50px; background: var(--card-white); }
  .front-body { position: relative; height: 222px; }
  .divider {
    position: absolute; left: 0; top: 0; width: 525px; height: 222px;
  }
  .brand {
    position: absolute; left: 38px; top: 52px; width: 210px;
    text-align: center; color: var(--brand-red);
  }
  .brand-mark {
    width: 34px; height: 34px; border-radius: 50%;
    background: var(--brand-red); margin: 0 auto 10px;
  }
  .brand-name {
    font-weight: 700; font-size: 27px; line-height: 1.02; letter-spacing: 0.5px;
    text-transform: uppercase;
  }
  .brand-phone {
    margin-top: 14px; font-weight: 700; font-size: 26px; color: var(--brand-red);
  }
  .contact {
    position: absolute; left: 292px; top: 34px; color: var(--ink);
  }
  .contact-name { font-weight: 700; font-size: 25px; color: var(--brand-red); }
  .contact-role { font-size: 16px; margin-top: 2px; margin-bottom: 16px; }
  .contact-line { display: flex; align-items: center; gap: 8px; font-size: 13.5px; margin-bottom: 8px; }
  .contact-line svg { flex: none; }
  .contact-address { font-size: 13.5px; line-height: 1.35; margin-top: 10px; }
  .front-band {
    height: 78px; background: var(--brand-red); color: var(--card-white);
    display: flex; flex-direction: column; justify-content: center; align-items: center;
    font-weight: 700; font-size: 23px; line-height: 1.2;
  }
  /* Back */
  .card-back {
    left: 625px; background: var(--brand-red); padding: 16px;
    display: grid; grid-template-columns: 1fr 1.1fr 1.1fr; grid-template-rows: 1fr 1fr; gap: 8px;
  }
  .photo { border-radius: 2px; }
  .photo-house { background: linear-gradient(160deg, #dfe4ea, var(--photo-grey)); }
  .photo-stair { background: linear-gradient(160deg, #8fa57a, #4f5a4c); }
  .photo-casement { background: linear-gradient(160deg, #f0dcb8, var(--photo-warm)); }
  .photo-forest { background: linear-gradient(160deg, #eef2ea, var(--photo-green)); }
  .photo-slider { background: linear-gradient(160deg, #f3efea, var(--photo-pale)); }
  .photo-french { background: linear-gradient(160deg, #f6f6f6, var(--photo-sky)); }
</style>
</head>
<body>

<section class="card card-front">
  <div class="front-body">
    <svg class="divider" viewBox="0 0 525 222" aria-hidden="true">
      <line x1="262" y1="40" x2="262" y2="200" stroke="#a8193a" stroke-width="1" opacity="0.6"/>
    </svg>
    <div class="brand">
      <div class="brand-mark"></div>
      <div class="brand-name">Bright<br>Frame<br>Masters</div>
      <div class="brand-phone">(555) 214-8630</div>
    </div>
    <div class="contact">
      <div class="contact-name">Colin Mercer</div>
      <div class="contact-role">Project Manager</div>
      <div class="contact-line">
        <svg width="16" height="12" viewBox="0 0 16 12" aria-hidden="true"><rect width="16" height="12" rx="1" fill="#a8193a"/><path d="M1 1 L8 7 L15 1" fill="none" stroke="#fff" stroke-width="1.4"/></svg>
        <span>colin@brightframemastersco.com</span>
      </div>
      <div class="contact-line">
        <svg width="16" height="16" viewBox="0 0 16 16" aria-hidden="true"><circle cx="8" cy="8" r="7.5" fill="#a8193a"/><path d="M1 8 H15 M8 1 C4 5 4 11 8 15 M8 1 C12 5 12 11 8 15" fill="none" stroke="#fff" stroke-width="1"/></svg>
        <span>www.brightframemastersco.com</span>
      </div>
      <div class="contact-address">421, Address line goes here<br>45452, Country name</div>
    </div>
  </div>
  <div class="front-band">
    <span>Window and Door Company</span>
    <span>Commercial and Residential</span>
  </div>
</section>

<section class="card card-back">
  <div class="photo photo-house" role="img" aria-label="Photo of a house front with white windows and iron railing"></div>
  <div class="photo photo-stair" role="img" aria-label="Photo of a bright interior with a tall gridded glass door wall"></div>
  <div class="photo photo-casement" role="img" aria-label="Photo of open wooden and white casement window frames"></div>
  <div class="photo photo-forest" role="img" aria-label="Photo of open white windows looking onto a green forest path"></div>
  <div class="photo photo-slider" role="img" aria-label="Photo of white sliding patio doors in a pale room"></div>
  <div class="photo photo-french" role="img" aria-label="Photo of three wooden French doors with glass panes"></div>
</section>

</body>
</html>
```